Design a Business Card with a Vantrel Theme

I need a business card designed. Please incorporate my picture and somehow incorporate the look of the vantrel card (I sell vantrel insurance so when they look at my business card I want them to associate it)
Front needs to include:
Name
Licensed Insurance Broker
Phone Number
email address
Specializing in Vantrel Prime Plans, Vantrel Supplements and Prescription Drug Plans

Back needs to include:
The highest compliment you can give me is the referral of your friend or loved ones...
Appointment Date/Time
(Please also include a picture/image of a Vantrel Card AND a Orla-Bex Card)

If you have any questions please let me know

Please do not use the logo on the vantrel card (it is copyrighted) You can use the logo in the "vantrel files" if you want.

```html
<!DOCTYPE html>
<html lang="en">
<head>
<meta charset="utf-8">
<title>Vantrel Health Insurance – Business Card</title>
<link rel="stylesheet" href="https://fonts.googleapis.com/css2?family=Marcellus&family=Montserrat:wght@500;600;700;800&display=swap">
<style>
  :root {
    --backdrop: #3d3e45;
    --card-black: #111111;
    --gold: #e1b93a;
    --gold-deep: #c99a2e;
    --ink: #111111;
    --text-light: #f1f1f1;
    --photo-light: #ececec;
    --photo-dark: #3a3a3a;
  }
  * { box-sizing: border-box; margin: 0; padding: 0; }
  html, body {
    width: 1200px; height: 900px; overflow: hidden;
    background: var(--backdrop);
    font-family: "Montserrat", Arial, sans-serif;
  }
  .canvas { position: relative; width: 1200px; height: 900px; }

  .card {
    position: absolute; left: 250px; width: 700px; height: 400px;
    background: var(--card-black);
    box-shadow: 0 18px 40px rgba(0,0,0,0.45);
    overflow: hidden;
  }
  .card--front { top: 40px; border: 4px solid var(--gold); }
  .card--back { top: 460px; }

  .brand-title {
    position: absolute; font-family: "Marcellus", Georgia, serif;
    color: var(--gold); text-transform: uppercase; letter-spacing: 1px;
  }
  .card--front .brand-title { left: 36px; top: 30px; font-size: 30px; }
  .card--back .brand-title { left: 40px; top: 42px; font-size: 30px; color: var(--gold-deep); }

  .portrait {
    position: absolute; left: 70px; top: 100px; width: 165px; height: 165px;
    border-radius: 50%;
    background: radial-gradient(circle at 50% 35%, var(--photo-light) 0 45%, var(--photo-dark) 46% 100%);
  }
  .person { position: absolute; left: 50px; top: 280px; width: 220px; text-align: center; }
  .person__name { color: var(--gold); font-weight: 800; font-size: 22px; letter-spacing: 0.5px; }
  .person__role { color: var(--gold); font-weight: 600; font-size: 13px; margin-top: 2px; }

  .accent-lines { position: absolute; left: 300px; top: 150px; }

  .info { position: absolute; left: 430px; top: 90px; width: 240px; color: var(--text-light); }
  .pill {
    display: inline-block; background: var(--gold); color: var(--ink);
    border-radius: 14px; padding: 5px 22px; font-weight: 600; font-size: 15px;
  }
  .contact-list { list-style: none; margin: 12px 0 26px 6px; }
  .contact-list li { display: flex; align-items: center; gap: 10px; font-size: 14px; margin-bottom: 8px; }
  .contact-list svg { flex: none; }
  .plans { list-style: none; margin: 10px 0 0 14px; font-size: 13px; line-height: 1.55; }

  .appointment { position: absolute; left: 140px; top: 120px; }
  .appointment .pill { font-family: "Marcellus", Georgia, serif; font-size: 24px; padding: 6px 26px; border-radius: 20px; }
  .slot { display: flex; align-items: flex-end; gap: 8px; color: var(--gold); font-size: 15px; font-weight: 500; margin-top: 18px; }
  .slot__line { width: 300px; border-bottom: 2px dotted var(--gold); height: 14px; }

  .referral-band {
    position: absolute; left: 0; bottom: 0; width: 100%; height: 96px;
    background: var(--gold); color: var(--ink);
    display: flex; align-items: center; padding: 0 40px;
    font-weight: 700; font-size: 19px; line-height: 1.3;
  }
</style>
</head>
<body>
<main class="canvas">

  <section class="card card--front" aria-label="Business card front">
    <h1 class="brand-title">Vantrel Health Insurance</h1>
    <div class="portrait" role="img" aria-label="Portrait photo of the broker"></div>
    <div class="person">
      <p class="person__name">DARREN KOLE</p>
      <p class="person__role">Licensed Insurance Broker</p>
    </div>
    <svg class="accent-lines" width="110" height="110" viewBox="0 0 110 110" aria-hidden="true">
      <g stroke="#e1b93a" stroke-width="2">
        <line x1="0" y1="10" x2="100" y2="60"/>
        <line x1="0" y1="22" x2="100" y2="72"/>
        <line x1="0" y1="34" x2="100" y2="84"/>
        <line x1="0" y1="46" x2="100" y2="96"/>
      </g>
    </svg>
    <div class="info">
      <span class="pill">CONTACT</span>
      <ul class="contact-list">
        <li>
          <svg width="18" height="18" viewBox="0 0 18 18" aria-hidden="true"><rect x="0.5" y="0.5" width="17" height="17" fill="none" stroke="#f1f1f1"/><path d="M5 4l2 0 1 3-1.5 1a7 7 0 0 0 3.5 3.5l1-1.5 3 1v2c0 1-1 1.5-2 1.2A10 10 0 0 1 4 6c-.3-1 .2-2 1-2z" fill="#f1f1f1"/></svg>
          <span>+660 555 41820</span>
        </li>
        <li>
          <svg width="18" height="18" viewBox="0 0 18 18" aria-hidden="true"><rect x="0.5" y="0.5" width="17" height="17" fill="none" stroke="#f1f1f1"/><rect x="3" y="5" width="12" height="8" fill="#f1f1f1"/><path d="M3 5l6 5 6-5" fill="none" stroke="#111" stroke-width="1.2"/></svg>
          <span>info@kolemail.com</span>
        </li>
      </ul>
      <span class="pill">Specializing in</span>
      <ul class="plans">
        <li>Vantrel Prime Plans</li>
        <li>Vantrel Supplements</li>
        <li>Prescription Drug Plans</li>
      </ul>
    </div>
  </section>

  <section class="card card--back" aria-label="Business card back">
    <h2 class="brand-title">Vantrel Health Insurance</h2>
    <div class="appointment">
      <span class="pill">APPOINTMENT</span>
      <div class="slot"><span>DATE :</span><span class="slot__line"></span></div>
      <div class="slot"><span>TIME :</span><span class="slot__line"></span></div>
    </div>
    <p class="referral-band">The highest compliment you can give me is the referral of<br>your friend or loved ones...</p>
  </section>

</main>
</body>
</html>
```